Zentrova - Creative Automation

We are a software house for Audio Visual Systems integration/automation and home automation. we develop innovative software to automate a variety of devices mainly related to audio visuals and we design touch panel user interfaces to control these systems.

We would like to see designs that stick to our colours and theme, which you can find on our webpage www.zentrova.com.au

The final design should communicate touch panels, innovation, software and automation.

Industry/Entity Type

Software

Requirements
Must have
• The business card must show the following information:
Name example : Derek Malloway
Qualification example: B Eng ICT(CompSys) Dip EngPrac
Title example : Control Systems Programmer
Mobile Phone, Company phone, Email address ,Company website

```html
<!DOCTYPE html>
<html lang="en">
<head>
<meta charset="utf-8">
<title>Zentrova - Business Card</title>
<link rel="stylesheet" href="https://fonts.googleapis.com/css2?family=Questrial&display=swap">
<style>
  :root {
    --backdrop: #d9d9d9;
    --card: #ffffff;
    --brand-green: #2eaa6a;
    --brand-blue: #2b86c9;
    --ink: #333333;
    --ink-soft: #6a6a6a;
  }
  html, body {
    margin: 0;
    padding: 0;
    width: 1200px;
    height: 871px;
    overflow: hidden;
    background: var(--backdrop);
    font-family: "Questrial", sans-serif;
  }
  .canvas {
    position: relative;
    width: 1200px;
    height: 871px;
  }
  .card {
    position: absolute;
    width: 620px;
    height: 354px;
    background: var(--card);
    box-shadow: 0 6px 18px rgba(0,0,0,0.18);
    overflow: hidden;
  }
  .card-front { left: 80px; top: 70px; }
  .card-back { left: 500px; top: 447px; }

  .brand {
    position: absolute;
    display: flex;
    align-items: center;
    gap: 12px;
  }
  .brand-mark {
    background: var(--brand-green);
    flex: none;
  }
  .brand-text { display: flex; flex-direction: column; }
  .brand-name {
    color: var(--brand-green);
    line-height: 1;
  }
  .brand-tagline {
    color: var(--ink-soft);
    text-align: right;
    margin-top: 2px;
  }

  .card-front .brand { left: 165px; top: 140px; }
  .card-front .brand-mark { width: 64px; height: 50px; }
  .card-front .brand-name { font-size: 56px; }
  .card-front .brand-tagline { font-size: 11px; }

  .card-back .brand { left: 38px; top: 120px; }
  .card-back .brand-mark { width: 46px; height: 36px; }
  .card-back .brand-name { font-size: 40px; }
  .card-back .brand-tagline { font-size: 8px; }

  .contact {
    position: absolute;
    left: 318px;
    top: 112px;
    color: var(--ink);
  }
  .contact-name {
    font-size: 21px;
    letter-spacing: 1.5px;
    margin: 0;
  }
  .contact-qual {
    font-size: 12px;
    letter-spacing: 0.5px;
    color: var(--ink-soft);
  }
  .contact-title {
    font-size: 13px;
    letter-spacing: 1.2px;
    color: var(--brand-green);
    margin: 2px 0 14px;
  }
  .contact-list {
    list-style: none;
    margin: 0;
    padding: 0;
    font-size: 13px;
    letter-spacing: 0.5px;
  }
  .contact-list li {
    display: flex;
    align-items: center;
    gap: 10px;
    margin-bottom: 8px;
  }
  .contact-list svg { width: 12px; height: 12px; fill: var(--brand-green); flex: none; }
  .contact-web {
    font-size: 13px;
    letter-spacing: 0.5px;
    color: var(--ink);
    margin-top: 4px;
  }
  .contact-web span { color: var(--brand-green); }

  .card-bands {
    position: absolute;
    left: 0;
    bottom: 0;
    width: 620px;
    height: 40px;
  }
</style>
</head>
<body>
<main class="canvas">

  <section class="card card-front" aria-label="Business card front">
    <div class="brand">
      <span class="brand-mark"></span>
      <div class="brand-text">
        <span class="brand-name">zentrova</span>
        <span class="brand-tagline">Creative Automation</span>
      </div>
    </div>
  </section>

  <section class="card card-back" aria-label="Business card back">
    <div class="brand">
      <span class="brand-mark"></span>
      <div class="brand-text">
        <span class="brand-name">zentrova</span>
        <span class="brand-tagline">Creative Automation</span>
      </div>
    </div>

    <div class="contact">
      <h1 class="contact-name">Derek Malloway, <span class="contact-qual">B Eng ICT</span></h1>
      <p class="contact-title">Control Systems Programmer</p>
      <ul class="contact-list">
        <li>
          <svg viewBox="0 0 12 12" aria-hidden="true"><path d="M1 4c0-2 2-3 5-3s5 1 5 3v1H8.5V3.8C7.8 3.5 4.2 3.5 3.5 3.8V5H1z M2.5 6h7l1 5h-9z"/></svg>
          1.800.555.0142
        </li>
        <li>
          <svg viewBox="0 0 12 12" aria-hidden="true"><path d="M3.5 0h5a1 1 0 0 1 1 1v10a1 1 0 0 1-1 1h-5a1 1 0 0 1-1-1V1a1 1 0 0 1 1-1zM4 1.5v7.5h4V1.5z"/></svg>
          604.555.0187
        </li>
        <li>
          <svg viewBox="0 0 12 12" aria-hidden="true"><path d="M0 2h12v8H0z M1 3l5 4 5-4" stroke="#fff" stroke-width="0.8"/></svg>
          derek@zentrova.ca
        </li>
      </ul>
      <p class="contact-web">www.<span>zentrova</span>.ca</p>
    </div>

    <svg class="card-bands" viewBox="0 0 620 40" aria-hidden="true">
      <rect x="0" y="22" width="300" height="18" fill="var(--brand-green)"/>
      <path d="M280 40 V26 Q280 16 294 16 H620 V40 Z" fill="var(--brand-blue)"/>
    </svg>
  </section>

</main>
</body>
</html>
```